The Velvet Magpie business card

I need a business card for my makeup artist business. I specialise in bridal, glamour, formal and special occasion makeup.
I am a mobile makeup artist who caters for every from nowra to sydney.
I do the following services:
Bridal makeup
airbrush makeup
special occasion
formals
hens nights/ girls night
makeup lesson
makeup for all ages from flower girl to Nanna of the bride!
photoshoot makeup
SPFX

I would like the card to portray a very professional sleek makeup business. I would also like another version of the card directed especially towards brides.

Please see my website to understand colours etc www.thevelvetmagpie.com

Industry/Entity Type

Business

Contact Information for Business Card

The Velvet Magpie
Professional Makeup Artist
Marguerite Olvey
0412083946
info@thevelvetmagpie.com
www.thevelvetmagpie.com
www.pagelink.net/thevelvetmagpie

```html
<!DOCTYPE html>
<html lang="en">
<head>
<meta charset="utf-8">
<title>The Velvet Magpie – Business Card</title>
<link href="https://fonts.googleapis.com/css2?family=Ubuntu:wght@400;500&family=Ubuntu+Condensed&family=Yellowtail&display=swap" rel="stylesheet">
<style>
  :root {
    --backdrop: #e8e5e3;
    --paper: #ffffff;
    --magenta: #a3195b;
    --magenta-deep: #6e0f3c;
    --plum: #5c1638;
    --plum-dark: #3b0a21;
    --pink: #e27aaa;
    --ink: #3a2230;
  }
  * { box-sizing: border-box; margin: 0; padding: 0; }
  html, body { width: 1200px; height: 873px; overflow: hidden; }
  body { background: var(--backdrop); position: relative; }

  .card {
    position: absolute;
    left: 280px;
    width: 640px;
    height: 388px;
    background: var(--paper);
    overflow: hidden;
    box-shadow: 0 6px 18px rgba(0,0,0,.12);
  }
  .card--front { top: 28px; }
  .card--back  { top: 457px; }

  /* Front */
  .band { position: absolute; top: 0; left: 0; width: 640px; height: 90px; }
  .artist-name {
    position: absolute; right: 42px; top: 6px;
    font-family: "Yellowtail", cursive;
    font-size: 36px; line-height: 46px; color: #fff;
  }
  .artist-role {
    position: absolute; right: 46px; top: 54px;
    font-family: "Ubuntu", sans-serif;
    font-size: 10px; color: #fff; letter-spacing: .3px;
  }
  .brand {
    position: absolute; left: 52px; top: 140px;
    font-family: "Ubuntu", sans-serif; font-weight: 500;
    font-size: 56px; line-height: 64px; color: var(--plum);
    white-space: nowrap;
  }
  .contacts {
    position: absolute; left: 52px; top: 252px;
    list-style: none;
    font-family: "Ubuntu", sans-serif; font-size: 15px; color: var(--ink);
  }
  .contacts li { display: flex; align-items: center; gap: 8px; height: 22px; }
  .contacts svg { width: 13px; height: 13px; flex: none; }
  .lipstick-art {
    position: absolute; right: 48px; top: 250px;
    width: 56px; height: 80px;
    background: linear-gradient(160deg, #c9a0ad 0%, #8a3a5c 55%, #5c1638 100%);
    border-radius: 6px;
  }

  /* Back */
  .services {
    position: absolute; left: 178px; top: 42px;
    width: 304px; height: 304px; border-radius: 50%;
    background: var(--plum-dark);
    display: flex; flex-direction: column; justify-content: center; align-items: center;
    list-style: none; text-align: center;
    font-family: "Ubuntu Condensed", sans-serif; font-size: 17px; line-height: 21px;
    z-index: 2;
  }
  .services .accent { color: var(--pink); }
  .services .plain  { color: #fff; }
  .gloss-art {
    position: absolute; left: 40px; bottom: 36px;
    width: 150px; height: 64px;
    background: linear-gradient(90deg, #d9c3cb, #7a2a4d 60%, #4a1029);
    border-radius: 10px;
  }
  .compact-art {
    position: absolute; right: 44px; top: 30px;
    width: 150px; height: 130px;
    background: radial-gradient(circle at 45% 45%, #f2ebee 0%, #c7a8b4 60%, #6e2d4a 100%);
    border-radius: 50%;
  }
</style>
</head>
<body>

<section class="card card--front">
  <svg class="band" viewBox="0 0 640 90" aria-hidden="true">
    <defs>
      <linearGradient id="bandFill" x1="0" x2="1" y1="0" y2="0">
        <stop offset="0" stop-color="#6e0f3c"/>
        <stop offset="1" stop-color="#a3195b"/>
      </linearGradient>
    </defs>
    <path d="M0,0 H640 V86 C470,74 220,46 0,30 Z" fill="url(#bandFill)"/>
  </svg>
  <p class="artist-name">Marguerite Olvey</p>
  <p class="artist-role">Professional Makeup Artist</p>

  <h1 class="brand">The Velvet Magpie</h1>

  <ul class="contacts">
    <li>
      <svg viewBox="0 0 14 14" aria-hidden="true"><circle cx="7" cy="7" r="7" fill="#3a2230"/><path d="M4.5 3.5l1.5 0 .6 2-1 .8a5 5 0 0 0 2.2 2.2l.8-1 2 .6v1.5c0 .5-.4.9-.9.9A6.3 6.3 0 0 1 3.6 4.4c0-.5.4-.9.9-.9z" fill="#fff"/></svg>
      0412083946
    </li>
    <li>
      <svg viewBox="0 0 14 14" aria-hidden="true"><circle cx="7" cy="7" r="7" fill="#3a2230"/><circle cx="7" cy="7" r="2" fill="none" stroke="#fff" stroke-width="1.2"/><path d="M9 7v1a1.2 1.2 0 0 0 2.2.4A4.2 4.2 0 1 0 9.5 10.3" fill="none" stroke="#fff" stroke-width="1.2"/></svg>
      info@thevelvetmagpie.com
    </li>
    <li>
      <svg viewBox="0 0 14 14" aria-hidden="true"><circle cx="7" cy="7" r="7" fill="#3a2230"/><circle cx="7" cy="7" r="4" fill="none" stroke="#fff" stroke-width="1"/><path d="M3 7h8M7 3c-2 2.3-2 5.7 0 8M7 3c2 2.3 2 5.7 0 8" fill="none" stroke="#fff" stroke-width="1"/></svg>
      www.thevelvetmagpie.com
    </li>
    <li>
      <svg viewBox="0 0 14 14" aria-hidden="true"><circle cx="7" cy="7" r="7" fill="#3a2230"/></svg>
      www.pagelink.net/thevelvetmagpie
    </li>
  </ul>

  <div class="lipstick-art" role="img" aria-label="Illustration of an open lipstick"></div>
</section>

<section class="card card--back">
  <div class="gloss-art" role="img" aria-label="Illustration of a lip gloss tube and wand"></div>
  <div class="compact-art" role="img" aria-label="Illustration of an open powder compact"></div>
  <ul class="services">
    <li class="accent">Bridal makeup</li>
    <li class="plain">Airbrush makeup</li>
    <li class="accent">Special occasion</li>
    <li class="plain">Formals</li>
    <li class="accent">Hens nights/ girls night</li>
    <li class="plain">Makeup lesson</li>
    <li class="accent">Makeup for all ages from</li>
    <li class="accent">flower girl to Nanna of the</li>
    <li class="plain">bride!</li>
    <li class="plain">Photoshoot makeup</li>
    <li class="accent">SPFX</li>
  </ul>
</section>

</body>
</html>
```